Résumé app needs 1 more template

Hi, I need 1 more template for my résumé app. The résumé app can be used in a browser (https://brightquill.com/resume-app) on an Koravo / Tabrix (https://apps.orvantel.com/app/id583726104) or on an Vellumos (https://market.tindrel.com/store/apps/details?id=com.brightquill.resume). The app lets the user create a résumé. It currently let's the user choose between 3 templates. I need 1 more. Please use the app first so you know how it will work.

Reason: Need more designs

Target Market(s)

Users of the app

Colors

Designer to choose colors to be used in the design.

Requirements
Must have
• original
• beautiful
• the resume template contains the data that the user can currently enter in the app (so do NOT design new features like sliders for level of experience etc)

```html
<!DOCTYPE html>
<html lang="en">
<head>
<meta charset="utf-8">
<title>Résumé Template</title>
<link href="https://fonts.googleapis.com/css2?family=Arimo:wght@400;700&display=swap" rel="stylesheet">
<style>
  :root {
    --backdrop: #dcdddf;
    --paper: #ffffff;
    --ink: #231f20;
    --ink-soft: #2b2b2b;
    --band: #231f20;
    --band-text: #ffffff;
    --photo-a: #8d8f93;
    --photo-b: #4e5054;
  }
  * { box-sizing: border-box; margin: 0; padding: 0; }
  html, body {
    width: 891px; height: 1200px; overflow: hidden;
    background: var(--backdrop);
    font-family: "Arimo", Arial, sans-serif;
    color: var(--ink);
  }
  .resume {
    position: absolute; left: 74px; top: 74px;
    width: 744px; height: 1053px;
    background: var(--paper);
    box-shadow: 0 0 3px rgba(0,0,0,0.12);
  }
  .portrait {
    position: absolute; left: 36px; top: 36px;
    width: 92px; height: 92px; border-radius: 4px;
    background: linear-gradient(160deg, var(--photo-a), var(--photo-b));
  }
  .identity { position: absolute; left: 146px; top: 62px; }
  .identity__name { font-size: 24px; font-weight: 700; line-height: 28px; letter-spacing: -0.2px; }
  .identity__role { font-size: 14px; line-height: 18px; margin-top: 1px; }
  .contact {
    position: absolute; left: 524px; top: 36px;
    width: 220px; height: 91px;
    background: var(--band); color: var(--band-text);
    text-align: right; padding: 16px 36px 0 0;
    font-size: 12px; font-weight: 700; line-height: 15px;
    font-style: normal;
  }
  .contact__address { margin-bottom: 5px; }
  .contact__line { display: flex; justify-content: flex-end; align-items: center; gap: 4px; }
  .contact__icon { width: 9px; height: 9px; fill: var(--band-text); flex: none; }
  .text {
    font-size: 12px; line-height: 16.6px; color: var(--ink-soft);
    white-space: nowrap;
  }
  .intro { position: absolute; left: 36px; top: 142px; }
  .section-title {
    position: absolute; left: 36px;
    font-size: 16px; font-weight: 700; line-height: 18px; letter-spacing: -0.2px;
  }
  .section-rule {
    position: absolute; left: 0; width: 708px; height: 4px;
    background: var(--ink);
  }
  .entries { position: absolute; left: 36px; width: 708px; }
  .entry { height: 120px; position: relative; }
  .entry__title { font-size: 14px; font-weight: 700; line-height: 18px; }
  .entry__meta { font-size: 13.5px; line-height: 19px; }
  .entry__body { margin-top: 4px; }
  .entry::after {
    content: ""; position: absolute; left: 0; right: 0; top: 105px;
    height: 1.6px; background: var(--ink);
  }
</style>
</head>
<body>
<main class="resume">
  <div class="portrait" role="img" aria-label="Portrait photo of the résumé owner"></div>

  <header class="identity">
    <h1 class="identity__name">Your Name</h1>
    <p class="identity__role">Profession</p>
  </header>

  <address class="contact">
    <div class="contact__address">1234 Larkmoor Lane NW<br>Fenwold, ST 00000</div>
    <div class="contact__line">name@fenwold.example
      <svg class="contact__icon" viewBox="0 0 10 10" aria-hidden="true"><path d="M2.2 0.5 3.8 2.6 2.9 3.7C3.6 5.1 4.9 6.4 6.3 7.1L7.4 6.2 9.5 7.8 8.6 9.4C4.4 9.2 0.8 5.6 0.6 1.4Z"/></svg>
    </div>
    <div class="contact__line">000.555.0100
      <svg class="contact__icon" viewBox="0 0 10 10" aria-hidden="true"><path d="M0 1.5h10v7H0Z"/><path d="M0.6 2 5 5.5 9.4 2" stroke="var(--band)" stroke-width="0.9" fill="none"/></svg>
    </div>
  </address>

  <p class="text intro">Lorem ipsum dolor sit amet, consectetur adipiscing elit. Sed commodo sit amet lacus eu rutrum. Phasellus vel dolor lobortis,<br>pulvinar velit vel, egestas mauris. Orci varius natoque penatibus et magnis dis parturient montes, nascetur ridiculus mus.<br>Aliquam finibus at est sed dapibus. Donec pulvinar ultricies facilisis. Aliquam auctor sit amet eros ut sagittis. Nunc placerat<br>quis leo in pellentesque usce molestie sed ipsum sit amet cphasellus eu nulla ut velit maximus aliquam sed molestie ipsum.<br>Mauris feugiat tincidunt pharetra. Pellentesque lorem turpis, hendrerit et aliquet sit amet, facilisis at ante integer posuere.</p>

  <h2 class="section-title" style="top:253px">EXPERIENCES</h2>
  <div class="section-rule" style="top:273px"></div>
  <section class="entries" style="top:293px">
    <article class="entry">
      <h3 class="entry__title">Title</h3>
      <p class="entry__meta">Company Name (May 2016 — present)</p>
      <p class="text entry__body">Lorem ipsum dolor sit amet, consectetur adipiscing elit. Sed commodo sit amet lacus eu rutrum. Phasellus vel dolor lobortis,<br>pulvinar velit vel, egestas mauris. Orci varius natoque penatibus et magnis dis parturient montes, nascetur ridiculus mus.<br>Aliquam finibus at est sed dapibus. Donec pulvinar ultricies facilisis. Aliquam auctor sit amet eros ut sagittis nunc placerat.</p>
    </article>
    <article class="entry">
      <h3 class="entry__title">Title</h3>
      <p class="entry__meta">Company Name (September 2013 — April 2016)</p>
      <p class="text entry__body">Lorem ipsum dolor sit amet, consectetur adipiscing elit. Sed commodo sit amet lacus eu rutrum. Phasellus vel dolor lobortis,<br>pulvinar velit vel, egestas mauris. Orci varius natoque penatibus et magnis dis parturient montes, nascetur ridiculus mus.<br>Aliquam finibus at est sed dapibus. Donec pulvinar ultricies facilisis. Aliquam auctor sit amet eros ut sagittis nunc placerat.</p>
    </article>
  </section>

  <h2 class="section-title" style="top:569px">EDUCATIONS</h2>
  <div class="section-rule" style="top:589px"></div>
  <section class="entries" style="top:609px">
    <article class="entry">
      <h3 class="entry__title">Degree</h3>
      <p class="entry__meta">School Name (September 2011 — June 2013)</p>
      <p class="text entry__body">Lorem ipsum dolor sit amet, consectetur adipiscing elit. Sed commodo sit amet lacus eu rutrum. Phasellus vel dolor lobortis,<br>pulvinar velit vel, egestas mauris. Orci varius natoque penatibus et magnis dis parturient montes, nascetur ridiculus mus.<br>Aliquam finibus at est sed dapibus. Donec pulvinar ultricies facilisis. Aliquam auctor sit amet eros ut sagittis nunc placerat.</p>
    </article>
    <article class="entry">
      <h3 class="entry__title">Degree</h3>
      <p class="entry__meta">School Name (September 2007 — June 2011)</p>
      <p class="text entry__body">Lorem ipsum dolor sit amet, consectetur adipiscing elit. Sed commodo sit amet lacus eu rutrum. Phasellus vel dolor lobortis,<br>pulvinar velit vel, egestas mauris. Orci varius natoque penatibus et magnis dis parturient montes, nascetur ridiculus mus.<br>Aliquam finibus at est sed dapibus. Donec pulvinar ultricies facilisis. Aliquam auctor sit amet eros ut sagittis nunc placerat.</p>
    </article>
  </section>

  <h2 class="section-title" style="top:885px">SOMETHING ELSE</h2>
  <div class="section-rule" style="top:905px"></div>
  <p class="text intro" style="top:925px">Lorem ipsum dolor sit amet, consectetur adipiscing elit. Sed commodo sit amet lacus eu rutrum. Phasellus vel dolor lobortis,<br>pulvinar velit vel, egestas mauris. Orci varius natoque penatibus et magnis dis parturient montes, nascetur ridiculus mus.<br>Aliquam finibus at est sed dapibus. Donec pulvinar ultricies facilisis. Aliquam auctor sit amet eros ut sagittis. Nunc placerat<br>quis leo in pellentesque usce molestie sed ipsum sit amet cphasellus eu nulla ut velit maximus aliquam sed molestie ipsum.<br>Mauris feugiat tincidunt pharetra. Pellentesque lorem turpis, hendrerit et aliquet sit amet, facilisis at ante integer posuere.</p>
</main>
</body>
</html>
```